eBook book cover for erotic novel set in Singapore (yes really!)

Hello - here’s a bit of background on my book, along with some thoughts on the cover. I hope this helps; am happy to answer any questions and provide further example chapters if that would help you get a better idea of what it’s all about (some extracts are attached to this brief).

1. "Under Quiet Lanterns" - synopsis
“I'm curious—and tempted. Oh dear!” is Bea’s reply to an advert posted on the internet and she enters into a relationship unlike any other she has experienced before—one that stimulates, frustrates, consumes and ultimately, delights, her.

Owen a successful banker living in Singapore has placed an online invitation for “irregular intimacy” with a “sexy, well-dressed lover with stimulating kinks”. Bea’s feeling dulled by her demanding job and the undemanding social rituals of her life in Singapore: she’s attracted to Owen’s slightly jaded urbanity and quirky ways. He finds her plain-speaking exuberance a refreshing contrast to his own more conservative nature.

After a sparky, and at times, spiky, email exchange they meet at a rooftop bar in Singapore’s Chinatown. Over cocktails they agree the seven rules of their relationship (the first one—“No questions about work or personal lives”). Despite this formality, the sexual attraction between them is intense—as is the sex when they first manage to schedule it. Over subsequent weeks they craft a list of sexual experiences they intend to enjoy together. Once they’ve completed ‘The List’ (on an Excel spreadsheet) they’ll part. That’s the intention anyway.

As their relationship develops they both can’t help applying their controlling corporate selves to their secret life. Apart from the proposed experiences on the agreed list, each of them sometimes introduces new things to surprise the other. Under Quiet Lanterns is set mainly in Singapore—where the exotic sights, sounds and tastes provide a sensual backdrop to the increasingly intense affair.

The novel is about two people who believe they can manage their relationship in the same way they organise everything else in their lives—with closely calibrated calendar entries, tightly planned sexual liaisons and multiple lists. They relish the contrasts between their demanding jobs (the frequent travel, late night conference calls and always-on Quillphones) and indulging their imaginations with someone they trust. Bea begins to appreciate just what being “sex fit” entails. The sex scenes are explicit (“Sex where she did things she couldn’t tell her sisters about”) and driven in part by their competitive natures.

However, it gradually becomes clear that it is becoming harder for them to contain their relationship to just sex, no matter how delightful. They had both originally committed to a ‘no strings attached’ affair but they struggle with their growing feelings for each other. Owen initially drives the relationship but increasingly becomes out of his depth whilst Bea gains confidence. The novel ends with over half The List still to be completed—will they be able to keep to the rules, and more importantly, maintain the expected emotional distance they’ve both agreed to?

2. Cover thoughts
I’d like to avoid the typical cliched image of say, a silk tie and handcuffs, that one often sees on book covers of this genre. A reference to Singapore/Asia would be good of course (an orchid too obvious?), and naturally being an ebook, the cover needs to be simple and striking. I have a second book planned, and half written, and possibly a third. A design that thus lends itself to being adapted slightly so as to support a trilogy would be particularly useful.

3. Author's name
Gus Palmer

Thanks
Gus

Women 25-45

Serif
Decorative
Script

85cae6
3176b5

• A reference to Asia/Singapore
• A sense of the unknown, reference to Asia/Singapore, a hint of sex attraction, reference to corporate life.
• Just had a thought that a single stiletto shoe (on a carpet, wooden floorboards?) might be interesting.
• Be overly explicit sexually - have the usual cliche of a scantily clad woman for example

```html
<!DOCTYPE html>
<html lang="en">
<head>
<meta charset="utf-8">
<title>Under Quiet Lanterns — Cover Wrap</title>
<link href="https://fonts.googleapis.com/css2?family=Oswald:wght@600;700&family=Montserrat:wght@700;800&display=swap" rel="stylesheet">
<style>
  :root {
    --stage: #e6e6e6;
    --paper: #f2f2f2;
    --spine-paper: #ececec;
    --ink-red: #951b1e;
    --ink-deep: #7a0f12;
    --box-red: #7d0c0f;
    --box-text: #f2e6e6;
    --shoe-red: #b3161c;
    --shoe-nude: #d9b48f;
  }
  * { box-sizing: border-box; margin: 0; padding: 0; }
  html, body { width: 1200px; height: 800px; overflow: hidden; background: var(--stage); }
  .cover-wrap {
    position: absolute; left: 203px; top: 100px;
    width: 794px; height: 600px;
    display: flex;
    box-shadow: 0 10px 30px rgba(0,0,0,0.12);
  }
  .back-cover {
    width: 380px; height: 100%;
    background: var(--paper);
    padding: 34px 26px 30px;
    position: relative;
  }
  .back-author {
    text-align: right;
    font-family: "Montserrat", sans-serif; font-weight: 800;
    font-size: 11px; letter-spacing: 0.3em;
    color: var(--ink-deep);
  }
  .back-title {
    text-align: right; white-space: nowrap;
    font-family: "Oswald", sans-serif; font-weight: 700;
    font-size: 33px; line-height: 1; letter-spacing: 0.01em;
    text-transform: uppercase;
    color: var(--ink-deep);
    margin-top: 2px;
  }
  .back-blurb {
    margin-top: 14px;
    font-family: "Montserrat", sans-serif; font-weight: 700;
    font-size: 8.2px; line-height: 1.42;
    text-align: justify; text-align-last: center;
    color: var(--ink-red);
  }
  .back-box {
    position: absolute; bottom: 30px;
    width: 92px; height: 56px;
    background: var(--box-red);
    color: var(--box-text);
    font-family: "Montserrat", sans-serif; font-weight: 700; font-size: 8px;
    display: flex; align-items: center; justify-content: center;
  }
  .back-box.publisher-mark { left: 34px; }
  .back-box.isbn-slot { right: 26px; }
  .spine {
    width: 34px; height: 100%;
    background: var(--spine-paper);
    display: flex; flex-direction: column; align-items: center;
    padding: 18px 0;
    border-left: 1px solid #dcdcdc; border-right: 1px solid #dcdcdc;
  }
  .spine-title, .spine-author {
    writing-mode: vertical-rl;
    color: var(--ink-red);
    text-transform: uppercase;
  }
  .spine-title {
    font-family: "Oswald", sans-serif; font-weight: 700;
    font-size: 18px; letter-spacing: 0.08em;
  }
  .spine-author {
    margin-top: auto;
    font-family: "Montserrat", sans-serif; font-weight: 800;
    font-size: 8px; letter-spacing: 0.45em;
  }
  .front-cover {
    width: 380px; height: 100%;
    background: var(--paper);
    position: relative;
  }
  .front-title {
    position: absolute; top: 26px; left: 0; width: 100%;
    text-align: center;
    font-family: "Oswald", sans-serif; font-weight: 700;
    font-size: 78px; line-height: 0.98;
    text-transform: uppercase;
    color: var(--ink-red);
  }
  .hero-shoe {
    position: absolute; left: 66px; top: 282px;
    width: 222px; height: 268px;
    border-radius: 40px 40px 30px 30px;
    background: radial-gradient(ellipse at 55% 45%, var(--shoe-nude) 0%, var(--shoe-red) 42%, rgba(179,22,28,0.35) 70%, rgba(242,242,242,0) 100%);
  }
  .front-author {
    position: absolute; bottom: 20px; left: 0; width: 100%;
    text-align: center;
    font-family: "Montserrat", sans-serif; font-weight: 800;
    font-size: 13px; letter-spacing: 0.32em;
    text-transform: uppercase;
    color: var(--ink-deep);
  }
</style>
</head>
<body>
  <main class="cover-wrap">
    <section class="back-cover">
      <p class="back-author">GUS PALMER</p>
      <h2 class="back-title">Under Quiet Lanterns</h2>
      <p class="back-blurb">Lorem ipsum dolor sit amet, consectetur adipisicing elit, sed do eiusmod tempor incididunt ut labore et dolore magna aliqua. Ut enim ad minim veniam, quis nostrud exercitation. Lorem ipsum dolor sit amet, consectetur adipisicing elit, sed do eiusmod tempor incididunt ut labore et dolore magna aliqua. Ut enim ad minim veniam, quis nostrud exercitation. Lorem ipsum dolor sit amet, consectetur adipisicing elit, sed do eiusmod tempor incididunt ut labore et dolore magna aliqua. Ut enim ad minim veniam, quis nostrud exercitation. Lorem ipsum dolor sit amet, consectetur adipisicing elit, sed do eiusmod tempor incididunt ut labore et dolore magna aliqua. Ut enim ad minim veniam, quis nostrud exercitation. Lorem ipsum dolor sit amet, consectetur adipisicing elit, sed do eiusmod tempor incididunt ut labore et dolore magna aliqua. Ut enim ad minim veniam, quis nostrud exercitation. Lorem ipsum dolor sit amet, consectetur adipisicing elit, sed do eiusmod tempor incididunt ut labore et dolore magna aliqua. Ut enim ad minim veniam, quis nostrud exercitation. Lorem ipsum dolor sit amet, consectetur adipisicing elit, sed do eiusmod tempor incididunt ut labore et dolore magna aliqua. Ut enim ad minim veniam, quis nostrud exercitation. Lorem ipsum dolor sit amet, consectetur adipisicing elit, sed do eiusmod tempor incididunt ut labore et dolore magna aliqua. Ut enim ad minim veniam, quis nostrud exercitation. Lorem ipsum dolor sit amet, consectetur adipisicing elit, sed do eiusmod tempor incididunt ut labore et dolore magna aliqua. Ut enim ad minim veniam, quis nostrud exercitation.</p>
      <div class="back-box publisher-mark">LOGO</div>
      <div class="back-box isbn-slot">ISBN</div>
    </section>
    <section class="spine">
      <span class="spine-title">Under Quiet Lanterns</span>
      <span class="spine-author">Gus Palmer</span>
    </section>
    <section class="front-cover">
      <h1 class="front-title">Under<br>Quiet<br>Lanterns</h1>
      <div class="hero-shoe" role="img" aria-label="Photograph of a single glossy red patent-leather stiletto pump with a nude lining"></div>
      <p class="front-author">Gus Palmer</p>
    </section>
  </main>
</body>
</html>
```